[WEB DESIGN - Start-up] Online LOANS against Luxury Assets - Needs a Web Design

Hello,
We need a web design for a new company. We make online LOANS against Luxury assets.
The name is private, that's why you could remplace it by the term "LOGO" or "ENTERPRISE".

In attachments, you'll find few models that we would like. Nonetheless, we don't want a copy of these screenshots. They are only prototypes that we made. Here we expect you to lead a professional web Design with your intuition and your ideas.

The final design should communicate start-up spirit, professionalism and fluidity.

Best Regards.

Industry/Entity Type

Finance

Number of Pages Required

2 page

Font styles to use
Sans Serif

Colors
f78f20
ffffff
b2b2b2
e9e9e9

Requirements
Must have
• The designer will draw on the 2015 web trends.
• The subject site is serious (loans against luxury assets), but the site should be modern and pleasant.
• PLEASE REFER YOU TO MY MODEL ( ATTACHMENTS)
Nice to have
• Surprise-me ! Welcome to a lot of imagination.

```html
<!DOCTYPE html>
<html lang="fr">
<head>
<meta charset="utf-8">
<title>Valoria – Prêts contre biens de luxe</title>
<link rel="stylesheet" href="https://fonts.googleapis.com/css2?family=Oswald:wght@400;600;700&family=Roboto:wght@300;400;500;700&display=swap">
<style>
:root{
  --orange:#f78f20;
  --white:#ffffff;
  --grey:#b2b2b2;
  --light:#e9e9e9;
  --dark:#1f1f1f;
  --darker:#161616;
  --text:#555555;
  --muted:#8a8a8a;
}
*{box-sizing:border-box;margin:0;padding:0}
html,body{width:1200px;height:2868px;overflow:hidden}
body{font-family:"Roboto",Arial,sans-serif;color:var(--text);background:var(--white);position:relative}
.abs{position:absolute}

/* header */
.site-header{position:absolute;left:0;top:0;width:1200px;height:64px;background:var(--darker)}
.brand{position:absolute;left:40px;top:14px;font:700 34px/36px "Oswald",sans-serif;color:var(--white);letter-spacing:1px}
.main-nav{position:absolute;right:40px;top:0;display:flex;height:64px;align-items:center;gap:30px}
.main-nav a{font:500 13px "Roboto",sans-serif;color:var(--white);text-decoration:none;letter-spacing:.5px}
.main-nav a.active{color:var(--orange);border-bottom:2px solid var(--orange);padding-bottom:3px}

/* hero */
.hero{position:absolute;left:0;top:64px;width:1200px;height:536px;background:radial-gradient(ellipse at 52% 40%,#6b6b6b 0%,#2e2e2e 32%,#101010 70%)}
.hero-visual{position:absolute;left:420px;top:0;width:520px;height:420px;background:radial-gradient(ellipse at 50% 35%,#d8d8d8 0%,#8a8a8a 30%,rgba(40,40,40,0) 70%)}
.hero-arrow{position:absolute;top:250px;color:var(--white);font:300 30px sans-serif;opacity:.7}
.estimate-form{position:absolute;left:112px;top:30px;width:230px;background:rgba(0,0,0,.55);padding:14px 12px}
.estimate-form h2{font:400 18px "Roboto",sans-serif;color:var(--white);margin-bottom:10px}
.field{height:24px;background:var(--white);margin-bottom:8px;font-size:10px;color:var(--grey);padding:6px 8px}
.btn{display:inline-block;background:var(--orange);color:var(--white);font:700 11px "Roboto",sans-serif;padding:8px 12px;margin-top:4px}
.hero-title{position:absolute;left:0;width:1200px;top:414px;text-align:center;font:700 36px/42px "Oswald",sans-serif;color:var(--white);text-transform:uppercase}

/* steps */
.steps{position:absolute;left:100px;top:692px;width:1000px;display:flex;gap:24px}
.step{flex:1}
.step-tab{position:relative;height:42px;width:150px;background:var(--orange);color:var(--white);padding:5px 10px}
.step-tab::after{content:"";position:absolute;right:-20px;top:0;border-left:20px solid var(--orange);border-top:21px solid transparent;border-bottom:21px solid transparent}
.step-tab small{display:block;font-size:9px}
.step-tab strong{font:700 14px "Roboto",sans-serif}
.step-line{height:2px;background:var(--orange);margin-top:-2px}
.step p{font-size:11px;line-height:16px;color:var(--muted);margin-top:10px}

/* assets */
.section-title{position:absolute;left:0;width:1200px;text-align:center;font:700 20px "Roboto",sans-serif;color:#333;text-transform:uppercase}
.assets{position:absolute;left:200px;top:984px;width:852px;display:grid;grid-template-columns:repeat(5,166px);grid-auto-rows:166px;gap:5px}
.asset{position:relative}
.asset span{position:absolute;left:0;right:0;bottom:10px;text-align:center;color:var(--white);font:500 12px "Roboto",sans-serif;text-shadow:0 1px 2px rgba(0,0,0,.6)}
.asset.faded{opacity:.35}
.carousel-arrow{position:absolute;top:1250px;color:#999;font:300 34px sans-serif}

/* help */
.help{position:absolute;left:0;top:1560px;width:1200px;height:470px;background:var(--light)}
.help h2{position:absolute;left:0;width:1200px;top:40px;text-align:center;color:var(--orange);font:700 22px "Roboto",sans-serif;text-transform:uppercase}
.help-cards{position:absolute;left:165px;top:120px;display:flex;gap:30px}
.help-card{width:270px;height:200px;background:var(--white);border:1px solid #dcdcdc;text-align:center;padding-top:26px}
.icon-circle{width:70px;height:70px;border-radius:50%;border:2px solid var(--light);margin:0 auto 24px;display:flex;align-items:center;justify-content:center}
.help-card small{display:block;font-size:10px;color:var(--muted)}
.help-card strong{display:block;font:500 13px "Roboto",sans-serif;color:var(--orange);margin-top:4px}

/* stats */
.leader-title{position:absolute;left:0;width:1200px;top:2070px;text-align:center;font:700 19px "Roboto",sans-serif;color:#333;text-transform:uppercase}
.col-title{position:absolute;font:500 17px "Roboto",sans-serif;color:var(--orange)}
.quote{position:absolute;left:100px;width:460px;height:88px;border:1px solid #ddd;padding:12px 16px;font-size:11px;line-height:16px;color:var(--muted)}
.author{position:absolute;left:100px;display:flex;align-items:center;gap:12px}
.avatar{width:44px;height:44px;border-radius:50%;background:linear-gradient(#d9c6b7,#8c7464)}
.author b{display:block;font-size:11px;color:#444}
.author small{font-size:10px;color:var(--muted)}
.counter{position:absolute;left:640px;display:flex;gap:6px}
.digit{width:44px;height:54px;background:linear-gradient(#3a3a3a 0 49%,#222 51%);color:var(--white);font:700 38px/54px "Oswald",sans-serif;text-align:center;border-radius:3px}
.stat-text{position:absolute;left:640px;width:460px;font-size:11px;line-height:16px;color:var(--muted)}

/* footer */
.site-footer{position:absolute;left:0;top:2620px;width:1200px;height:248px;background:var(--dark);color:#aaa}
.site-footer h3{position:absolute;left:100px;top:32px;font:500 20px "Roboto",sans-serif;color:var(--white)}
.footer-about{position:absolute;left:100px;top:70px;width:500px;font-size:11px;line-height:16px}
.footer-links{position:absolute;left:700px;top:34px;list-style:none;font-size:11px;line-height:17px}
.footer-contact{position:absolute;left:900px;top:34px;width:220px;font-size:11px;line-height:16px}
.copyright{position:absolute;left:900px;top:200px;font-size:10px;color:#888}
</style>
</head>
<body>

<header class="site-header">
  <div class="brand">VALORIA</div>
  <nav class="main-nav">
    <a class="active">CONCEPT</a><a>LES BIENS</a><a>ESTIMATION</a><a>FAQ</a><a>MON COMPTE</a><a>CALL : 04 00 00 00 00</a>
  </nav>
</header>

<section class="hero">
  <div class="hero-visual" role="img" aria-label="Bague en diamant sur fond sombre"></div>
  <div class="hero-arrow" style="left:24px">‹</div>
  <div class="hero-arrow" style="right:24px">›</div>
  <form class="estimate-form">
    <h2>Natures de l'objet</h2>
    <div class="field">Sélectionnez</div>
    <div class="field">Marque du bien</div>
    <div class="field">Année d'achat</div>
    <div class="field">Valeur estimée</div>
    <div class="field">Votre e-mail</div>
    <span class="btn">RECHERCHER</span>
  </form>
  <h1 class="hero-title">On se lasse de tout,<br>sauf de l'argent</h1>
</section>

<section class="steps">
  <div class="step"><div class="step-tab"><small>Step 1</small><strong>ESTIMATION</strong></div><div class="step-line"></div>
    <p>Décrivez votre bien en quelques clics et recevez une estimation gratuite de sa valeur par nos experts sous 24 heures.</p></div>
  <div class="step"><div class="step-tab"><small>Step 2</small><strong>PAIEMENT</strong></div><div class="step-line"></div>
    <p>Acceptez notre offre de prêt et recevez les fonds directement sur votre compte bancaire, rapidement et sans frais cachés.</p></div>
  <div class="step"><div class="step-tab"><small>Step 3</small><strong>SÉCURISATION</strong></div><div class="step-line"></div>
    <p>Votre bien est conservé dans un coffre sécurisé et assuré pendant toute la durée du prêt, en toute confidentialité.</p></div>
  <div class="step"><div class="step-tab"><small>Step 4</small><strong>RACHAT</strong></div><div class="step-line"></div>
    <p>Remboursez votre prêt à tout moment et récupérez votre bien dans son état d'origine, sans aucune pénalité.</p></div>
</section>

<h2 class="section-title" style="top:930px">Les beins que nous acceptons</h2>
<div class="carousel-arrow" style="left:160px">‹</div>
<div class="carousel-arrow" style="left:1068px">›</div>
<div class="assets">
  <div class="asset" role="img" aria-label="Tableau d'art" style="background:linear-gradient(135deg,#f7a23e,#c9620e)"><span>Art Tableaux</span></div>
  <div class="asset" role="img" aria-label="Pierres précieuses" style="background:linear-gradient(135deg,#6d6d6d,#1e1e1e)"><span>Pierres Précieuses</span></div>
  <div class="asset" role="img" aria-label="Vins et spiritueux" style="background:linear-gradient(135deg,#3b3b3b,#0d0d0d)"><span>Vins &amp; Spiritueux</span></div>
  <div class="asset" role="img" aria-label="Sculpture d'art graphique" style="background:linear-gradient(135deg,#e0d6c8,#a89a85)"><span>Art Graphique</span></div>
  <div class="asset faded" role="img" aria-label="Objet d'art" style="background:linear-gradient(135deg,#cfd8e0,#9aa7b2)"></div>
  <div class="asset" role="img" aria-label="Montre de luxe" style="background:linear-gradient(135deg,#5a5a5a,#151515)"><span>Montres</span></div>
  <div class="asset" role="img" aria-label="Voiture de prestige" style="background:linear-gradient(135deg,#9aa3ad,#2f353c)"><span>Véhicules</span></div>
  <div class="asset" role="img" aria-label="Pièces en métal précieux" style="background:linear-gradient(135deg,#c08a4a,#6b4520)"><span>Métaux Précieux</span></div>
  <div class="asset" role="img" aria-label="Sac de maroquinerie" style="background:linear-gradient(135deg,#b07a4a,#5a3418)"><span>Maroquinerie</span></div>
  <div class="asset faded" role="img" aria-label="Objet de collection" style="background:linear-gradient(135deg,#d8d8d8,#a0a0a0)"></div>
  <div class="asset" role="img" aria-label="Instrument de musique" style="background:linear-gradient(135deg,#d4d4d4,#8c8c8c)"><span>Instruments</span></div>
  <div class="asset" role="img" aria-label="Bijoux" style="background:linear-gradient(135deg,#a27a5e,#3a2418)"><span>Bijoux</span></div>
  <div class="asset" role="img" aria-label="Équipement high-tech" style="background:linear-gradient(135deg,#2c4f7a,#0e1a2c)"><span>High-Technology Equipments</span></div>
  <div class="asset" role="img" aria-label="Machinerie" style="background:linear-gradient(135deg,#7a7a7a,#3a3a3a)"><span>Machinerie</span></div>
  <div class="asset faded" role="img" aria-label="Objet de collection" style="background:linear-gradient(135deg,#e2e2e2,#b2b2b2)"></div>
</div>

<section class="help">
  <h2>Besoin d'aide? Nous sommes à votre écoute</h2>
  <div class="help-cards">
    <div class="help-card">
      <div class="icon-circle"><svg width="28" height="28" viewBox="0 0 24 24" fill="#b2b2b2"><path d="M6.6 10.8a15 15 0 0 0 6.6 6.6l2.2-2.2a1 1 0 0 1 1-.25 11.4 11.4 0 0 0 3.6.57 1 1 0 0 1 1 1V20a1 1 0 0 1-1 1A17 17 0 0 1 3 4a1 1 0 0 1 1-1h3.5a1 1 0 0 1 1 1c0 1.25.2 2.45.57 3.57a1 1 0 0 1-.25 1z"/></svg></div>
      <small>Nous sommes joignables 7j/7</small><strong>01 40 00 12 34</strong>
    </div>
    <div class="help-card">
      <div class="icon-circle"><span style="font:700 30px Roboto,sans-serif;color:#b2b2b2">?</span></div>
      <small>Toutes les réponses à vos questions</small><strong>Questions Fréquentes</strong>
    </div>
    <div class="help-card">
      <div class="icon-circle"><svg width="30" height="22" viewBox="0 0 30 22" fill="none" stroke="#b2b2b2" stroke-width="2"><rect x="1" y="1" width="28" height="20"/><path d="M1 1l14 11L29 1"/></svg></div>
      <small>Écrivez-nous à tout moment</small><strong>Formulaire de contact<br>ou<br>contact@valoria-gage.fr</strong>
    </div>
  </div>
</section>

<h2 class="leader-title">Entreprise est no1 de la vcente avec facult de rach at</h2>
<h3 class="col-title" style="left:100px;top:2130px">Derniers Témoignages</h3>
<h3 class="col-title" style="left:640px;top:2130px">Quelques Chiffres</h3>

<div class="quote" style="top:2170px">« Service rapide et très professionnel. J'ai obtenu mon prêt en deux jours et récupéré ma montre sans aucune difficulté. Je recommande vivement cette équipe à l'écoute. »</div>
<div class="author" style="top:2272px"><div class="avatar" role="img" aria-label="Photo du client"></div><div><b>Marc D.</b><small>Client depuis 2014, Paris</small></div></div>
<div class="quote" style="top:2410px">« Une solution discrète et efficace pour obtenir de la trésorerie. L'estimation était juste et les conseillers ont répondu à toutes mes questions. Merci encore. »</div>
<div class="author" style="top:2512px"><div class="avatar" role="img" aria-label="Photo de la cliente"></div><div><b>Claire M.</b><small>Cliente depuis 2015, Lyon</small></div></div>

<div class="counter" style="top:2170px"><div class="digit">0</div><div class="digit">5</div><div class="digit">3</div><div class="digit">1</div><div class="digit">9</div></div>
<p class="stat-text" style="top:2240px">Biens estimés par nos experts depuis la création de notre service. Chaque objet est examiné avec soin afin de vous proposer la meilleure offre de prêt possible, en toute transparence et sans engagement de votre part.</p>
<div class="counter" style="top:2400px"><div class="digit">0</div><div class="digit">4</div><div class="digit">8</div><div class="digit">0</div><div class="digit">8</div></div>
<p class="stat-text" style="top:2470px">Prêts accordés à nos clients satisfaits. Nos solutions de financement souples vous permettent d'obtenir rapidement des liquidités tout en conservant la possibilité de racheter votre bien à tout moment.</p>

<footer class="site-footer">
  <h3>Vendre en vue de racheter</h3>
  <p class="footer-about">Nous vous proposons une solution simple et rapide pour obtenir des liquidités grâce à vos biens de valeur. Confiez-nous votre objet, recevez votre argent et rachetez-le quand vous le souhaitez. Nos experts garantissent une estimation juste, un stockage sécurisé et un service entièrement confidentiel pour chaque client.</p>
  <ul class="footer-links"><li>Accueil</li><li>Concept</li><li>Les biens</li><li>Estimation</li><li>FAQ</li><li>Mon compte</li><li>Nous contacter</li><li>Mentions légales</li><li>CGV</li></ul>
  <div class="footer-contact">VALORIA<br>12 rue des Artisans<br>75000 Paris<br>Tél. : 01 40 00 12 34<br><br>Société au capital de 50 000 euros, immatriculée au registre du commerce.</div>
  <div class="copyright">Copyright © 2015 Valoria. Tous droits réservés.</div>
</footer>

</body>
</html>
```